Consulting company needs Business Cards - rough concept provided

I'm looking for someone to take our business card idea and make is slick and polished - to communicate our high-end, sophisticated, serious consulting business. We have a rough layout we did in-house. We are open to ideas on repo-ing elements, adjusting sizes, typefaces etc... within the general concept we've already come up with. We want it to be super-clean and sophisticated. We want to keep the white backgrounds, and blue brand colors. Our goal is to print with painted blue edges on thick cardstock. Thank you!!

```html
<!DOCTYPE html>
<html lang="en">
<head>
<meta charset="utf-8">
<title>North Harbor – Business Card</title>
<link rel="stylesheet" href="https://fonts.googleapis.com/css2?family=Poppins:wght@400;500;600;700&family=Montserrat:wght@300;400;600&display=swap">
<style>
  :root {
    --backdrop: #575757;
    --card: #ffffff;
    --brand-blue: #0a9add;
    --ink: #111111;
    --rule: #333333;
  }
  * { margin: 0; padding: 0; box-sizing: border-box; }
  html, body { width: 862px; height: 1200px; overflow: hidden; }
  body {
    background: var(--backdrop);
    font-family: "Poppins", sans-serif;
    color: var(--ink);
    position: relative;
  }
  .card {
    position: absolute;
    left: 96px;
    width: 670px;
    height: 383px;
    background: var(--card);
    box-shadow: 0 10px 40px rgba(0,0,0,.35);
    overflow: hidden;
  }
  .card--front { top: 137px; }
  .card--back { top: 680px; }

  .corner-blue-top { position: absolute; left: 536px; top: 0; right: 0; height: 13px; background: var(--brand-blue); }
  .corner-blue-side { position: absolute; right: 0; top: 0; width: 15px; height: 130px; background: var(--brand-blue); }
  .corner-black-side { position: absolute; left: 0; top: 250px; width: 15px; bottom: 0; background: #000; }
  .corner-black-bottom { position: absolute; left: 0; bottom: 0; width: 134px; height: 15px; background: #000; }

  .brand-name {
    position: absolute;
    right: 55px;
    top: 48px;
    font-family: "Poppins", sans-serif;
    font-weight: 700;
    font-size: 29px;
    line-height: 1;
    letter-spacing: -0.5px;
    color: var(--brand-blue);
    white-space: nowrap;
  }

  .rule { position: absolute; height: 1px; background: var(--rule); }

  .person-name {
    position: absolute; left: 53px; top: 153px;
    font-weight: 600; font-size: 27px; line-height: 1; letter-spacing: -0.3px;
  }
  .person-name .surname { color: var(--brand-blue); }
  .person-title {
    position: absolute; left: 53px; top: 184px;
    font-size: 13.5px; font-weight: 400; line-height: 1; letter-spacing: 0.2px;
  }

  .contact {
    position: absolute;
    display: flex; align-items: flex-start; gap: 6px;
    font-size: 14.5px; line-height: 18px;
  }
  .contact svg { flex: none; width: 19px; height: 19px; }
  .contact--phone { left: 53px; top: 230px; }
  .contact--email { left: 53px; top: 254px; }
  .contact--address { left: 407px; top: 228px; }
  .contact--address .lines { line-height: 18px; }

  .mission {
    position: absolute; left: 40px; right: 40px; top: 118px;
    font-family: "Montserrat", sans-serif;
    font-weight: 300; font-size: 28px; line-height: 35.5px;
    text-align: center; color: #222;
  }
  .mission strong { font-weight: 600; color: var(--brand-blue); }

  .website {
    position: absolute; left: 67px; top: 298px;
    font-family: "Montserrat", sans-serif; font-weight: 400;
    font-size: 14.5px; letter-spacing: 3.6px; line-height: 1;
  }
</style>
</head>
<body>

<section class="card card--front" aria-label="Business card front">
  <div class="corner-blue-top"></div>
  <div class="corner-blue-side"></div>
  <div class="corner-black-side"></div>
  <div class="corner-black-bottom"></div>

  <div class="brand-name">NORTH HARBOR</div>

  <div class="rule" style="left:0;top:174px;width:49px;"></div>
  <h1 class="person-name">Dana <span class="surname">Whitfield</span></h1>
  <p class="person-title">BRAND CONSULTANT</p>
  <div class="rule" style="left:207px;top:193px;right:0;"></div>

  <div class="contact contact--phone">
    <svg viewBox="0 0 20 20" aria-hidden="true"><circle cx="10" cy="10" r="10" fill="var(--brand-blue)"/><path d="M6.4 5.2l2 .1.8 2.4-1.2 1a7 7 0 003.3 3.3l1-1.2 2.4.8.1 2c-.6.7-1.6 1-2.6.7A10 10 0 015.7 7.8c-.3-1 0-2 .7-2.6z" fill="#fff"/></svg>
    <span>(555) 014 2290</span>
  </div>
  <div class="contact contact--email">
    <svg viewBox="0 0 20 20" aria-hidden="true"><circle cx="10" cy="10" r="10" fill="var(--brand-blue)"/><rect x="5" y="6.5" width="10" height="7" rx="1" fill="#fff"/><path d="M5.4 7l4.6 3.6L14.6 7" fill="none" stroke="var(--brand-blue)" stroke-width="1"/></svg>
    <span>dana@northharbor.com</span>
  </div>
  <div class="contact contact--address">
    <svg viewBox="0 0 20 20" aria-hidden="true"><circle cx="10" cy="10" r="10" fill="var(--brand-blue)"/><path d="M10 4.5a3.5 3.5 0 00-3.5 3.5c0 2.6 3.5 6 3.5 6s3.5-3.4 3.5-6A3.5 3.5 0 0010 4.5z" fill="#fff"/><circle cx="10" cy="8" r="1.3" fill="var(--brand-blue)"/><path d="M6 14.5h8" stroke="#fff" stroke-width="1"/></svg>
    <span class="lines">4820 Linden Ave, Ste<br>210 Fairview, CA 90000</span>
  </div>
</section>

<section class="card card--back" aria-label="Business card back">
  <div class="corner-blue-top"></div>
  <div class="corner-blue-side"></div>
  <div class="corner-black-side"></div>
  <div class="corner-black-bottom"></div>

  <div class="rule" style="left:0;top:76px;width:401px;"></div>
  <div class="brand-name">NORTH HARBOR</div>

  <p class="mission">
    <strong>We help</strong> [target demographic]<br>
    <strong>achieve</strong> [desired emotional outcome]<br>
    <strong>by</strong> [our unique approach] <strong>because</strong><br>
    [our brand beliefs]
  </p>

  <p class="website">www.northharbor.com</p>
  <div class="rule" style="left:298px;top:311px;right:0;"></div>
</section>

</body>
</html>
```